Flyer for Brand New Montessori School

Quiet Harbor Academy is opening in the fall to students infant-5th grade. We need a catchy, professional flyer that will attract a very upscale clientele. Most of our students will be under the age of 5, but we want to attract older students as well. The project is to design a flyer that tells people about our school, and directs them to the website to enroll/get more information

Target Market(s)

Upscale, affluent parents who need care for and want to educate their children starting at a young age.

Industry/Entity Type

Education/Day Care

Font styles to use
Serif

Colors
59FF00
82FF00
B8FF75
E3FFCB
F4FFEA
6B429C
8869AF
B7A5CE
E3DAEB
F3F0F8

Requirements
Must have
• photos of children, a clean look
Nice to have
• Please see attached logo samples. I am going to use either 2a or 4a; those are the colors i would like to use
Should not have
• A cluttered look or too much information

```html
<!DOCTYPE html>
<html lang="en">
<head>
<meta charset="utf-8">
<title>Quiet Harbor Academy – Flyer</title>
<link href="https://fonts.googleapis.com/css2?family=Libre+Baskerville:wght@400;700&family=Open+Sans:wght@400;600;700;800&display=swap" rel="stylesheet">
<style>
:root{
  --purple:#5a2a85;
  --purple-deep:#4a1f72;
  --green:#3d9c2b;
  --green-bright:#4db82f;
  --orange:#e3891c;
  --panel:#ececec;
  --ink:#333;
  --white:#fff;
  --bg:#e6e6e6;
}
*{box-sizing:border-box;margin:0;padding:0}
html,body{width:1200px;height:2755px;overflow:hidden;background:var(--bg);font-family:"Open Sans",Arial,sans-serif;color:var(--ink)}
.page{position:absolute;left:80px;width:1040px;height:1340px;background:var(--white);overflow:hidden;box-shadow:0 6px 24px rgba(0,0,0,.15)}
.page-front{top:25px}
.page-back{top:1390px}
.abs{position:absolute}

/* wordmark */
.brand{display:flex;align-items:center;gap:16px}
.brand-dot{width:70px;height:70px;border-radius:50%;background:var(--purple);flex:none}
.brand-name{color:var(--purple);font-weight:800;font-size:38px;line-height:1;text-transform:uppercase;letter-spacing:-.5px}
.page-front .brand{left:330px;top:55px}

/* photo + band */
.hero-band{left:0;top:470px;width:1040px;height:210px;background:var(--purple)}
.hero-photo{left:92px;top:180px;width:868px;height:380px;border-radius:60px;background:linear-gradient(120deg,#cfe6ef 0%,#e9d7b8 40%,#f3c88a 60%,#8fc0da 100%)}
.hero-title{left:0;top:590px;width:1040px;text-align:center;color:var(--white);font-family:"Libre Baskerville",Georgia,serif;font-size:27px;line-height:1.3}

/* body copy */
.intro{top:705px;left:57px;width:930px;display:grid;grid-template-columns:1fr 1fr;gap:38px;font-size:10.5px;line-height:1.45}
.intro p{margin-bottom:8px}

/* community panel */
.community{left:57px;top:885px;width:910px;height:355px;background:var(--panel);border-radius:34px}
.community-tab{left:225px;top:-4px;width:460px;height:40px;background:var(--purple);color:var(--white);border-radius:0 0 22px 22px;font-weight:700;font-size:17px;text-align:center;line-height:40px;white-space:nowrap}
.community-copy{left:28px;top:60px;width:405px;font-size:10.5px;line-height:1.45}
.founder-photo{left:28px;top:205px;width:135px;height:135px;border-radius:50%;border:5px solid var(--white);background:radial-gradient(circle at 50% 40%,#d9b49a,#3b2a2a 75%)}
.founder-name{left:185px;top:235px;color:var(--purple);font-weight:700;font-size:22px;line-height:1.15}
.founder-role{left:185px;top:292px;font-size:9.5px;color:#555}
.perks{left:455px;top:55px;width:430px;list-style:none;font-size:11px;line-height:1.35}
.perks li{position:relative;padding-left:20px;margin-bottom:9px;font-weight:700}
.perks li::before,.checks li::before{content:"✓";position:absolute;left:0;top:1px;width:13px;height:13px;border-radius:50%;background:var(--green);color:var(--white);font-size:9px;line-height:13px;text-align:center;font-weight:700}
.perks small{display:block;font-weight:400;font-size:10px;margin-top:3px}
.perks .sub{font-weight:400;padding-left:34px}
.perks .sub::before{left:14px}

/* footer */
.footer-green{left:0;top:1180px;width:520px;height:160px;background:var(--green)}
.footer-purple{left:520px;top:1180px;width:520px;height:160px;background:var(--purple)}
.more-pill{left:57px;top:1250px;width:430px;height:60px;border-radius:30px;background:var(--purple);color:var(--white);font-weight:800;font-size:30px;line-height:60px;text-align:center}
.url{left:560px;top:1266px;color:var(--white);font-weight:700;font-size:25px}

/* back page */
.page-back .brand{left:70px;top:50px}
.page-back .brand-name{font-size:36px}
.key-tab{left:437px;top:25px;width:603px;height:140px;background:var(--purple);border-radius:70px 0 0 70px}
.key-title{right:115px;top:40px;text-align:right;color:var(--white);font-weight:700;font-size:24px;line-height:1.3;text-transform:uppercase}
.key-bar{left:945px;top:45px;width:8px;height:100px;background:var(--green-bright)}

.pillar{left:70px;width:265px;color:var(--white);font-weight:700;font-size:26px;text-transform:uppercase;text-align:center;line-height:1.25;display:flex;align-items:center;justify-content:center}
.pillar-program{top:195px;height:255px;background:var(--orange);clip-path:polygon(0 0,100% 0,100% 82%,50% 100%,0 82%)}
.pillar-family{top:405px;height:285px;background:var(--green);clip-path:polygon(0 0,50% 16%,100% 0,100% 84%,50% 100%,0 84%)}
.pillar-team{top:645px;height:350px;background:var(--purple);clip-path:polygon(0 0,50% 13%,100% 0,100% 87%,50% 100%,0 87%)}
.pillar span{display:block}
.pillar-program span{margin-top:-20px}
.pillar-team span{margin-top:20px}

.bracket{left:335px;width:610px;border-top:3px solid;border-right:3px solid;border-radius:0 34px 34px 0;border-bottom:3px solid}
.bracket::after{content:"";position:absolute;right:-9px;bottom:-9px;width:15px;height:15px;border-radius:50%;background:currentColor}
.bracket-orange{top:190px;height:230px;color:var(--orange);border-color:var(--orange)}
.bracket-green{top:420px;height:270px;color:var(--green);border-color:var(--green)}
.bracket-purple{top:700px;height:290px;color:var(--purple);border-color:var(--purple)}
.bracket-orange,.bracket-green,.bracket-purple{border-bottom-color:transparent}

.checks{list-style:none;left:375px;width:555px;font-size:18px;line-height:1.35;color:#222}
.checks li{position:relative;padding-left:30px;margin-bottom:8px}
.checks li::before{width:17px;height:17px;font-size:11px;line-height:17px;top:4px}
.checks-program{top:220px}
.checks-family{top:455px}
.checks-team{top:735px}

.card{top:1015px;width:290px;height:225px;background:var(--white);border:4px solid #d6d6d6;border-radius:0 0 26px 26px;box-shadow:0 4px 10px rgba(0,0,0,.2);padding:14px 18px}
.card h3{color:var(--purple);font-size:21px;font-weight:800;text-align:center;text-transform:uppercase;margin-bottom:12px}
.card ul{list-style:none;font-size:12.5px;line-height:1.3}
.card li{position:relative;padding-left:22px;margin-bottom:9px}
.card li::before{content:"✓";position:absolute;left:0;top:1px;width:14px;height:14px;border-radius:50%;background:var(--green);color:var(--white);font-size:9px;line-height:14px;text-align:center;font-weight:700}
.card-students{left:60px}
.card-staff{left:372px}
.card-families{left:684px}
</style>
</head>
<body>

<section class="page page-front">
  <div class="abs brand">
    <span class="brand-dot"></span>
    <span class="brand-name">Quiet Harbor<br>Academy</span>
  </div>

  <div class="abs hero-band"></div>
  <div class="abs hero-photo" role="img" aria-label="Photo of three smiling school children holding books"></div>
  <h1 class="abs hero-title">Give your child an advanced start at Quiet Harbor Academy!<br>Montessori Education for Tomorrow’s Global Leaders</h1>

  <div class="abs intro">
    <div>
      <p>Quiet Harbor Academy educates infants through 5th grade students, using the renowned Montessori approach to education. Montessori education helps students develop the skills and talents that lead to remarkable future success.</p>
      <p>Our students achieve academic excellence, learn independence and discover a natural love for learning. Students develop respect for self and others and a global mindset. We employ a research-based, neurologically informed program that promotes brain development, social skills, problem solving and creativity. We expect that our students will achieve success and change the world.</p>
    </div>
    <div>
      <p>Students are taught in a manner that allows each one to accept new challenges once they have mastered a skill. Students are allowed to grow and advance at their own pace. In addition to core academic subjects, students also have classes in Art, Music, Physical Education, Language and Life Skills.</p>
      <p>Our teachers are experienced and caring professionals who are experts in their field. We searched far and wide to find the best educators to teach our students.</p>
      <p>Enroll your child today and give them the gift of an advanced start to their educational journey.</p>
    </div>
  </div>

  <div class="abs footer-green"></div>
  <div class="abs footer-purple"></div>

  <div class="abs community">
    <div class="abs community-tab">Join a community of parents just like you!</div>
    <p class="abs community-copy">The Quiet Harbor Academy community is composed of like-minded parents who value education and who will do anything to make sure that their children have every available resource. We all want the best for our children. We are here for you! We want to make sure that parents have a first class experience and feel confident in their child’s success.</p>
    <div class="abs founder-photo" role="img" aria-label="Portrait photo of the school founder"></div>
    <div class="abs founder-name">Elena<br>Marsh Whitford</div>
    <div class="abs founder-role">Quiet Harbor Academy Founder</div>
    <ul class="abs perks">
      <li>Top notch, high performing, highly educated teachers</li>
      <li class="sub">Multi-stage classes that challenge students to work hard and succeed, starting with infants</li>
      <li>Professional operations that value customer service and are designed to meet the needs of busy families</li>
      <li>Parent education and coaching and access to an educational concierge</li>
      <li>State of the art facility designed to best meet the needs of students</li>
      <li>Solid leadership team with more than 20 years of experience starting and leading schools</li>
      <li>Extended hours<small>An extended calendar with minimal days that we are closed and a promise to be open whenever it is possible</small></li>
      <li class="sub">Frequent, effective communication that includes newsletters, phone calls, text messages, social media posts and face-to-face interactions with teachers and staff</li>
    </ul>
  </div>

  <div class="abs more-pill">For more Information</div>
  <div class="abs url">www.quietharborschool.com</div>
</section>

<section class="page page-back">
  <div class="abs brand">
    <span class="brand-dot"></span>
    <span class="brand-name">Quiet Harbor<br>Academy</span>
  </div>
  <div class="abs key-tab"></div>
  <h2 class="abs key-title">Key Characteristics<br>that differentiate Quiet<br>Harbor Academy</h2>
  <div class="abs key-bar"></div>

  <div class="abs bracket bracket-orange"></div>
  <div class="abs bracket bracket-green"></div>
  <div class="abs bracket bracket-purple"></div>

  <div class="abs pillar pillar-program"><span>Customized<br>Educational<br>Program</span></div>
  <div class="abs pillar pillar-family"><span>Family<br>Support</span></div>
  <div class="abs pillar pillar-team"><span>Top<br>Notch<br>Team</span></div>

  <ul class="abs checks checks-program">
    <li>Begin with infants-utilize every precious moment</li>
    <li>Montessori Curriculum</li>
    <li>Critical thinking, Creativity, Academic Skill</li>
    <li>Problem Solving, Language, Compassion</li>
    <li>Research and Neurologically based</li>
  </ul>
  <ul class="abs checks checks-family">
    <li>Welcoming atmosphere for parents as partners</li>
    <li>Provide answers for parents in all areas of parenting</li>
    <li>Create community of like-minded parents</li>
    <li>High levels of customer service</li>
    <li>Engage other caring adults and multi-generational families</li>
    <li>Redefine expectations for education</li>
    <li>Help student achieve potential</li>
  </ul>
  <ul class="abs checks checks-team">
    <li>Talented, best in class professional teachers</li>
    <li>Team that is balanced around desired characteristics</li>
    <li>Opportunity to provide input and shape future of the school</li>
    <li>Great compensation, profit sharing and robust professional development opportunities</li>
    <li>Experienced school leader with 25+ years experience in best schools in the country</li>
  </ul>

  <div class="abs footer-green"></div>
  <div class="abs footer-purple"></div>

  <div class="abs card card-students">
    <h3>Students</h3>
    <ul>
      <li>Challenged and loved</li>
      <li>Close Relationship with Teachers</li>
      <li>Alignment between school, home and family</li>
      <li>Personalized learning at own pace</li>
    </ul>
  </div>
  <div class="abs card card-staff">
    <h3>Staff</h3>
    <ul>
      <li>Strengths and unique abilities leveraged</li>
      <li>Valued as professionals</li>
      <li>Mutual Investment</li>
      <li>Close relationship with students and families</li>
    </ul>
  </div>
  <div class="abs card card-families">
    <h3>Families</h3>
    <ul>
      <li>School sets and meets high expectations</li>
      <li>Welcomed and invited to engage</li>
      <li>High levels of service and educational concierge</li>
      <li>Educated and coached on how to support child</li>
    </ul>
  </div>

  <div class="abs more-pill">For more Information</div>
  <div class="abs url">www.quietharborschool.com</div>
</section>

</body>
</html>
```